Kestrel Aid Services Banner Ad

Need a 750 x 250-pixel banner ad with the company Logo included. Please see company website at www.kestrelaidservices.com for more information.

```html
<!DOCTYPE html>
<html lang="en">
<head>
<meta charset="utf-8">
<title>Kestrel Aid Services Banner Ads</title>
<link href="https://fonts.googleapis.com/css2?family=Fira+Sans+Condensed:wght@500;600&display=swap" rel="stylesheet">
<style>
  :root {
    --page-bg: #f2f7fd;
    --white: #ffffff;
    --navy: #0d3a63;
    --green: #6cb21f;
    --text-grey: #454545;
    --shadow: 0 2px 6px rgba(0, 0, 0, 0.12);
  }
  * { margin: 0; padding: 0; box-sizing: border-box; }
  html, body {
    width: 1140px;
    height: 1200px;
    overflow: hidden;
    background: var(--page-bg);
    font-family: "Fira Sans Condensed", "Arial Narrow", sans-serif;
  }
  .stage {
    position: relative;
    width: 830px;
    height: 874px;
    transform: scale(1.3735);
    transform-origin: 0 0;
  }
  .banner {
    position: absolute;
    left: 34px;
    width: 750px;
    height: 250px;
    overflow: hidden;
    box-shadow: var(--shadow);
  }
  .banner--kids { top: 32px; background: var(--white); }
  .banner--paint { top: 312px; background: var(--navy); }
  .banner--friends { top: 582px; background: var(--white); }
  .banner-art { position: absolute; inset: 0; width: 750px; height: 250px; }

  .brand {
    display: flex;
    align-items: center;
    gap: 10px;
    font-weight: 600;
    font-size: 29px;
    line-height: 1;
    text-transform: uppercase;
    letter-spacing: 0.3px;
    white-space: nowrap;
  }
  .brand-dot { width: 22px; height: 22px; border-radius: 50%; flex: none; }
  .brand--green { color: var(--green); }
  .brand--green .brand-dot { background: var(--navy); }
  .brand--white { color: var(--white); }
  .brand--white .brand-dot { background: var(--white); }

  .tagline {
    font-weight: 500;
    font-size: 19px;
    letter-spacing: 0.1px;
    white-space: nowrap;
  }
  .values {
    display: flex;
    align-items: center;
    gap: 18px;
    list-style: none;
    color: var(--green);
    font-weight: 500;
    font-size: 19px;
    line-height: 1;
    white-space: nowrap;
  }
  .values .sep { width: 8px; height: 8px; margin: 0 5px; border-radius: 50%; flex: none; }
  .values--dark .sep { background: var(--navy); }
  .values--light .sep { background: var(--white); }

  .kids-copy {
    position: absolute;
    left: 340px; right: 10px; top: 58px;
    display: flex; flex-direction: column; align-items: center;
  }
  .kids-copy .tagline { color: var(--text-grey); margin-top: 34px; }
  .kids-copy .values { margin-top: 28px; }

  .paint-copy {
    position: absolute;
    left: 25px; top: 56px;
  }
  .paint-copy .tagline { color: var(--white); margin-top: 36px; }
  .paint-copy .values { margin-top: 20px; }

  .friends-copy {
    position: absolute;
    right: 26px; top: 48px;
    display: flex; flex-direction: column; align-items: flex-end;
  }
  .friends-copy .values { margin-top: 32px; }
</style>
</head>
<body>
<main class="stage">

  <section class="banner banner--kids">
    <svg class="banner-art" viewBox="0 0 750 250">
      <defs>
        <linearGradient id="kidsPhotoTone" x1="0" y1="0" x2="1" y2="1">
          <stop offset="0" stop-color="#9aa48c"/>
          <stop offset="0.5" stop-color="#d7827a"/>
          <stop offset="1" stop-color="#c0394a"/>
        </linearGradient>
      </defs>
      <path d="M255,0 C330,60 330,190 255,250 L272,250 C345,190 345,60 272,0 Z" fill="var(--green)"/>
      <path d="M0,0 L258,0 C332,60 332,190 258,250 L0,250 Z" fill="url(#kidsPhotoTone)" role="img" aria-label="Photo: smiling child in a knit hat and pink jacket climbing a rope net at a playground"/>
    </svg>
    <div class="kids-copy">
      <div class="brand brand--green"><span class="brand-dot"></span>Kestrel Aid Services</div>
      <p class="tagline">SUPPORT COORDINATION ACROSS NEW JERSEY</p>
      <ul class="values values--dark">
        <li>PARTNER</li><li class="sep"></li><li>EDUCATION</li><li class="sep"></li><li>COMMUNITY</li>
      </ul>
    </div>
  </section>

  <section class="banner banner--paint">
    <svg class="banner-art" viewBox="0 0 750 250">
      <defs>
        <linearGradient id="paintPhotoTone" x1="0" y1="0" x2="1" y2="1">
          <stop offset="0" stop-color="#d9b07a"/>
          <stop offset="0.5" stop-color="#e6b8b0"/>
          <stop offset="1" stop-color="#9a5a6a"/>
        </linearGradient>
      </defs>
      <polygon points="481,0 750,0 750,250 416,250" fill="var(--green)"/>
      <polygon points="490,0 750,0 750,250 425,250" fill="url(#paintPhotoTone)" role="img" aria-label="Photo: happy child showing hands covered in bright paint"/>
    </svg>
    <div class="paint-copy">
      <div class="brand brand--white"><span class="brand-dot"></span>Kestrel Aid Services</div>
      <p class="tagline">SUPPORT COORDINATION ACROSS NEW JERSEY</p>
      <ul class="values values--light">
        <li>PARTNER</li><li class="sep"></li><li>EDUCATION</li><li class="sep"></li><li>COMMUNITY</li>
      </ul>
    </div>
  </section>

  <section class="banner banner--friends">
    <svg class="banner-art" viewBox="0 0 750 250">
      <defs>
        <linearGradient id="friendsPhotoTone" x1="0" y1="0" x2="1" y2="0.6">
          <stop offset="0" stop-color="#d89a4a"/>
          <stop offset="0.45" stop-color="#8fb04a"/>
          <stop offset="1" stop-color="#4f8f2a"/>
        </linearGradient>
      </defs>
      <path d="M0,0 L95,0 C200,14 290,80 360,150 C430,215 540,222 750,168 L750,250 L0,250 Z" fill="var(--navy)"/>
      <path d="M0,26 C140,10 250,60 330,140 C380,190 450,235 520,250 L0,250 Z" fill="var(--green)"/>
      <path d="M0,42 C135,26 240,76 318,152 C365,198 430,237 492,250 L0,250 Z" fill="url(#friendsPhotoTone)" role="img" aria-label="Photo: two smiling friends embracing on a sunny lawn"/>
    </svg>
    <div class="friends-copy">
      <div class="brand brand--green"><span class="brand-dot"></span>Kestrel Aid Services</div>
      <ul class="values values--dark">
        <li>PARTNER</li><li class="sep"></li><li>EDUCATION</li><li class="sep"></li><li>COMMUNITY</li>
      </ul>
    </div>
  </section>

</main>
</body>
</html>
```